Corvane Sable - Advanced Skincare and undetectable Makeup for Men

We are in need of a professional webpage for our company Corvane Sable. We help every man feel his best by looking his best. Inspired by the myth of Corvane, we offer makeup and skincare products along with education upon their use. Our mission is to celebrate masculinity in all of its forms, regardless of age, race, sexual orientation, or assigned gender at birth.

The webpage would serve as our online store, as a place where our clients can learn about our brand, view our "How-to" video tutorials, and get product information. An online blog will also be hosted in order to keep clients up to date with news, updates, media mentions, etc.

The color schemes that we use are mostly Black and Gold, with Red accents. please keep in mind that this is a men's cosmetics line, and therefore should read powerful, sexy, confident and bold - all with a high end look and feel.

Think along the lines of brands like Len Barrow, QPT, Velcotti, etc.

our logo is included in the files attached. images and copy will be added in at a later time; hence, general images that fit the feel and filler text is encouraged.

The products to be sold include:
a face cleanser in a pump dispenser bottle (1 size)
a mask in a round jar container (1 size)
a moisturizer in a pump container 1 size)
a concealer in a click pen with a brush applicator (3 shades)
a liquid liner pen (4 shades)
a contouring palette (2 shade options)
a setting spray (single option)

Millennial Men

Beauty

5+ page

Serif

ec1f27
000000
faa54b

• ur essential requirements are:
• 1) a stunning and engaging landing page that truly captures the ideals of sexuality, boldness and confidence.
• 2) an interactive and engaging online store that is easy to update / add product / information to.
• 3) Product pages supporting various toggling images of the product, a shade selection option, ingredient information, usage instructions, pricing, and a link to a "how to video" unique to each individual product.
• 4) dedicated space where all of the tutorials can be organized together
• 5) an organized Blog section, that would include a segment for a Q&A section for us to update as the brand grows, ongoing contests (that would be easily hidden if there are no contests running at the moment) as well as general news and updates segment.
• 6) an "about us" page, where our customers are able to learn about our story, inspirations, humanitarian efforts and philosophies in product contents and purity.
• 7) a contact us page, which would include social media links, contact email and telephone number as well as physical address to be updated upon launch.
• 8) discrete privacy policy, terms of use, and return policy links available at the bottom of every page
• 1) A posting forum where clients could post their looks using our products, or maybe a live stream of our Picturloop account.
• 2) a member sign in page so that we can collect and store customer information for faster check out, keep track of purchases attached to their email address (future loyalty program plans) and maintain an email database for email notifications and the such.

```html
<!DOCTYPE html>
<html lang="en">
<head>
<meta charset="utf-8">
<title>Corvane Sable – Men's Skin Solutions</title>
<link href="https://fonts.googleapis.com/css2?family=Cinzel:wght@400;600;700&family=Montserrat:wght@600;800&family=Open+Sans:ital,wght@0,400;0,600;0,700;1,400&family=Oswald:wght@500;600&family=Playfair+Display:wght@700&display=swap" rel="stylesheet">
<style>
:root{
  --gold:#b07c2c;
  --gold-light:#c99a45;
  --gold-dark:#8a5e1c;
  --ink:#141414;
  --black:#0b0b0b;
  --grey:#6b6b6b;
  --line:#e4e4e4;
  --white:#ffffff;
}
*{margin:0;padding:0;box-sizing:border-box}
html,body{width:1200px;height:4675px;overflow:hidden;background:var(--white)}
body{position:relative;font-family:"Open Sans",Arial,sans-serif;color:var(--ink)}
.section-title{position:absolute;left:0;width:1200px;text-align:center;font-family:"Cinzel",serif;font-weight:700;color:var(--gold);font-size:38px;letter-spacing:1px}
.btn{position:absolute;display:flex;align-items:center;justify-content:center;background:var(--gold);color:var(--white);font-family:"Cinzel",serif;font-weight:700;border-radius:30px;letter-spacing:.5px}
.photo{position:absolute}

/* header */
.site-header{position:absolute;left:0;top:0;width:1200px;height:103px;background:var(--white)}
.brand{position:absolute;left:78px;top:30px;display:flex;align-items:center;gap:10px;font-family:"Cinzel",serif;font-weight:700;color:var(--gold);font-size:22px;letter-spacing:2px}
.brand-square{width:22px;height:22px;background:var(--gold)}
.util-links{position:absolute;right:78px;top:14px;font-size:13px;color:var(--ink)}
.util-links span{margin:0 8px;color:#999}
.main-nav{position:absolute;right:210px;top:60px;display:flex;gap:26px;font-size:14px;font-weight:600;letter-spacing:.5px}
.main-nav a{color:var(--ink);text-decoration:none;padding-bottom:6px}
.main-nav a.active{color:var(--gold);border-bottom:2px solid var(--gold)}
.sign-in{left:1004px;top:50px;width:118px;height:44px;font-size:16px;border:2px solid var(--gold-light)}

/* hero */
.hero{position:absolute;left:0;top:103px;width:1200px;height:573px;background:linear-gradient(100deg,#1d5b78 0%,#2a7a92 30%,#8a7560 55%,#c8b9a3 75%,#a9967b 100%)}
.hero-title{position:absolute;left:78px;top:150px;font-family:"Montserrat",sans-serif;font-weight:800;color:var(--white);font-size:82px;line-height:86px}
.hero-mission{position:absolute;left:80px;top:327px;width:540px;font-family:"Open Sans",sans-serif;font-weight:700;color:var(--white);font-size:18px;line-height:26px}
.hero-btn{left:78px;top:430px;width:218px;height:56px;font-size:17px}
.dots{position:absolute;display:flex;gap:6px}
.dots i{width:11px;height:11px;border-radius:50%;border:1.5px solid var(--white);display:block}
.dots i.on{background:var(--white)}

/* welcome */
.welcome-text{position:absolute;left:200px;top:800px;width:800px;text-align:center;font-size:14px;line-height:24px;color:var(--grey)}
.tile-label{position:absolute;font-family:"Oswald",sans-serif;font-weight:600;color:var(--black);font-size:30px;line-height:34px}
.feature-caption{position:absolute;left:570px;top:1275px;font-family:"Oswald",sans-serif;font-weight:500;color:var(--white);font-size:21px;line-height:26px}
.arrow-btn{position:absolute;width:44px;height:44px;border-radius:50%;background:rgba(255,255,255,.35);display:flex;align-items:center;justify-content:center}

/* products */
.products{position:absolute;left:78px;top:1415px;width:1044px;height:664px;background:radial-gradient(ellipse at center,#2a2622 0%,#141210 60%,#0a0908 100%)}
.products .section-title{width:1044px;top:50px}
.product{position:absolute;top:0;width:250px;text-align:center}
.product-img{position:absolute;left:45px;top:145px;width:160px;height:230px;background:linear-gradient(180deg,rgba(255,255,255,.06),rgba(255,255,255,.14))}
.product-name{position:absolute;left:0;width:250px;top:412px;font-family:"Cinzel",serif;font-weight:600;color:var(--white);font-size:16px;letter-spacing:.5px}
.stars{position:absolute;left:0;width:250px;top:434px;color:var(--gold-light);font-size:15px;letter-spacing:2px}
.price{position:absolute;left:0;width:250px;top:455px;font-family:"Cinzel",serif;font-weight:700;color:var(--white);font-size:32px}
.product .btn{left:27px;top:505px;width:196px;height:48px;font-size:16px}
.highlight{position:absolute;left:25px;top:130px;width:234px;height:264px;background:linear-gradient(180deg,#5a3f1e,#3a2811);border:1px solid #6d4c22}
.cart{position:absolute;left:78px;top:175px;width:50px;height:50px;border-radius:50%;background:var(--gold);display:flex;align-items:center;justify-content:center}

/* skincare */
.skincare-frame{position:absolute;left:380px;top:2170px;width:446px;height:392px;background:#5e5e5e}
.skincare-photo{left:358px;top:2144px;width:446px;height:396px;background:linear-gradient(160deg,#7aa3bd 0%,#c2d7e3 40%,#8a6b57 60%,#4f7e98 100%)}
.skincare-card{position:absolute;left:78px;top:2238px;width:262px;height:256px;background:var(--white);box-shadow:0 2px 12px rgba(0,0,0,.18);display:flex;align-items:center;justify-content:center;text-align:center;font-family:"Cinzel",serif;font-weight:700;color:var(--gold);font-size:22px;line-height:28px;padding:0 14px}
.checklist{position:absolute;left:870px;top:2165px;list-style:none}
.checklist li{display:flex;align-items:center;gap:14px;height:42px;font-size:14px;color:var(--ink)}

/* picturloop */
.follow-btn{left:508px;top:3005px;width:184px;height:46px;font-size:16px;gap:8px}
.tag{position:absolute;left:0;bottom:0;height:30px;padding:0 14px;display:flex;align-items:center;background:rgba(176,124,44,.9);color:var(--white);font-family:"Playfair Display",serif;font-style:italic;font-size:15px}
.insta{position:absolute;top:2693px;width:321px;height:290px}

/* testimonial */
.testimonial{position:absolute;left:0;top:3117px;width:1200px;height:362px;background:linear-gradient(90deg,#0d0d0d 0%,#2a2522 50%,#0d0d0d 100%)}
.testimonial .section-title{top:72px;font-size:36px}
.avatar{position:absolute;left:290px;top:150px;width:115px;height:115px;border-radius:50%;border:4px solid var(--white);background:linear-gradient(160deg,#8aa4b4,#c19a7d)}
.quote{position:absolute;left:440px;top:156px;width:665px;color:var(--white);font-size:14px;line-height:24px}
.client{position:absolute;left:440px;top:250px;font-family:"Cinzel",serif;color:var(--gold-light);font-size:14px;letter-spacing:1px}

/* blog */
.blog-card{position:absolute;top:3606px;height:415px;background:var(--white);box-shadow:0 2px 14px rgba(0,0,0,.12);text-align:center}
.blog-date{position:absolute;left:0;right:0;top:34px;display:flex;justify-content:center;align-items:center;gap:8px;font-family:"Playfair Display",serif;font-weight:700;color:var(--gold);font-size:16px}
.blog-title{position:absolute;left:20px;right:20px;top:76px;font-family:"Playfair Display",serif;font-weight:700;font-size:17px;line-height:24px;color:var(--ink)}
.blog-excerpt{position:absolute;left:30px;right:30px;top:144px;font-size:13px;line-height:21px;color:var(--grey)}
.blog-img{position:absolute;left:0;right:0;bottom:0;height:187px}
.blog-rule{position:absolute;left:20px;right:20px;top:64px;height:1px;background:var(--line)}

/* rewards */
.rewards{position:absolute;left:0;top:4083px;width:1200px;height:172px;background:var(--gold)}
.rewards h2{position:absolute;left:78px;top:36px;font-family:"Cinzel",serif;font-weight:700;color:var(--white);font-size:38px}
.rewards p{position:absolute;left:78px;top:88px;width:420px;font-size:13px;line-height:20px;color:var(--white)}
.email-field{position:absolute;left:508px;top:57px;width:422px;height:56px;border-radius:30px;background:var(--white);display:flex;align-items:center;padding-left:26px;font-size:14px;color:#777}
.subscribe{position:absolute;left:941px;top:57px;width:172px;height:56px;border-radius:30px;border:2px solid var(--white);display:flex;align-items:center;justify-content:center;font-family:"Cinzel",serif;font-weight:700;color:var(--white);font-size:18px}

/* footer */
.site-footer{position:absolute;left:0;top:4255px;width:1200px;height:420px;background:var(--black)}
.foot-col{position:absolute;top:42px}
.foot-col h4{font-family:"Cinzel",serif;font-weight:700;color:var(--white);font-size:16px;letter-spacing:.5px;margin-bottom:14px}
.foot-col ul{list-style:none}
.foot-col li{display:flex;align-items:center;gap:10px;height:29px;font-size:13px;color:#d8d8d8}
.foot-col li::before{content:"";width:5px;height:5px;border-radius:50%;background:var(--gold-light)}
.foot-col.social li{height:42px}
.foot-col.social li::before{display:none}
.social-dot{width:30px;height:30px;border-radius:50%;background:var(--gold);display:block}
.foot-brand{position:absolute;left:0;width:1200px;top:282px;display:flex;justify-content:center;align-items:center;gap:10px;font-family:"Cinzel",serif;font-weight:700;color:var(--gold);font-size:22px;letter-spacing:2px}
.copyright{position:absolute;left:0;width:1200px;top:370px;text-align:center;font-size:14px;color:var(--gold-light)}
</style>
</head>
<body>

<header class="site-header">
  <div class="brand"><span class="brand-square"></span>CORVANE SABLE</div>
  <div class="util-links">Men's Skin Solutions<span>|</span>Customer Care<span>|</span>My Account</div>
  <nav class="main-nav">
    <a class="active" href="#">HOME</a><a href="#">OUR STORE</a><a href="#">PRODUCTS</a><a href="#">BLOG</a><a href="#">ABOUT US</a><a href="#">CONTACT US</a>
  </nav>
  <div class="btn sign-in">
    <svg width="16" height="16" viewBox="0 0 16 16" style="margin-right:6px"><circle cx="8" cy="5" r="3.2" fill="#fff"/><path d="M2 15c0-3.5 2.7-5.5 6-5.5s6 2 6 5.5z" fill="#fff"/></svg>SIGN IN
  </div>
</header>

<section class="hero" role="img" aria-label="Shirtless man standing before a sea arch and rocky coastline">
  <h1 class="hero-title">CORVANE<br>SABLE</h1>
  <p class="hero-mission">Our Mission Is To Celebrate Masculinity In All Of Its Forms, Regardless Of Age, Race, Sexual Orientation, Or Assigned Gender At Birth</p>
  <div class="btn hero-btn">MORE ABOUT US</div>
  <div class="dots" style="left:565px;top:553px"><i class="on"></i><i></i><i></i><i></i></div>
</section>

<h2 class="section-title" style="top:732px">WELCOME TO CORVANE SABLE</h2>
<p class="welcome-text">Lorem Ipsum is simply dummy text of the printing and typesetting industry. Lorem Ipsum has been the industry's standard dummy text ever since the 1500s, when an unknown printer took a galley of type and scrambled it to make.</p>

<div class="photo" style="left:78px;top:876px;width:365px;height:231px;background:linear-gradient(110deg,#5a6d7c 0%,#9aa9b4 45%,#dcdfe2 100%)" role="img" aria-label="Man splashing water on his face with cleanser"></div>
<div class="tile-label" style="left:286px;top:900px">FACE<br>CLEANSER</div>
<div class="photo" style="left:78px;top:1119px;width:365px;height:231px;background:linear-gradient(110deg,#5b4a40 0%,#a08776 45%,#e6e3e0 100%)" role="img" aria-label="Man applying concealer pen under his eye"></div>
<div class="tile-label" style="left:286px;top:1143px">PEN<br>CONCEALER</div>
<div class="photo" style="left:461px;top:876px;width:661px;height:474px;background:linear-gradient(120deg,#1f1f1f 0%,#6a6a6a 40%,#bdbdbd 70%,#3a3a3a 100%)" role="img" aria-label="Black and white portrait of a bearded man running a hand through his hair"></div>
<div class="arrow-btn" style="left:482px;top:1272px"><svg width="14" height="14" viewBox="0 0 14 14"><path d="M9 2 4 7l5 5" stroke="#fff" stroke-width="2" fill="none"/></svg></div>
<div class="arrow-btn" style="left:1058px;top:1272px"><svg width="14" height="14" viewBox="0 0 14 14"><path d="M5 2l5 5-5 5" stroke="#fff" stroke-width="2" fill="none"/></svg></div>
<div class="feature-caption">PRODUCTS FORMULATED WITH THE<br>HIGHEST QUALITY NATURAL INGREDIENTS</div>

<section class="products">
  <h2 class="section-title">CORVANE SABLE PRODUCTS</h2>
  <div class="highlight"></div>
  <div class="product" style="left:6px">
    <div class="product-img" style="background:linear-gradient(180deg,rgba(230,150,50,.25),rgba(230,150,50,.45))" role="img" aria-label="Product photo: face cleanser pump bottle"></div>
    <div class="cart"><svg width="24" height="22" viewBox="0 0 24 22"><path d="M1 2h4l3 11h11l3-8H7" stroke="#fff" stroke-width="2" fill="none"/><circle cx="10" cy="18" r="2" fill="#fff"/><circle cx="18" cy="18" r="2" fill="#fff"/></svg></div>
    <div class="product-name">FACE CLEANSER</div><div class="stars">★★★★★</div><div class="price">$42.00</div>
    <div class="btn">HOW TO VIDEO</div>
  </div>
  <div class="product" style="left:258px">
    <div class="product-img" role="img" aria-label="Product photo: face mask jar"></div>
    <div class="product-name">MASK</div><div class="stars">★★★★★</div><div class="price">$42.00</div>
    <div class="btn">HOW TO VIDEO</div>
  </div>
  <div class="product" style="left:522px">
    <div class="product-img" role="img" aria-label="Product photo: moisturizer pump bottle"></div>
    <div class="product-name">MOISTURIZER</div><div class="stars">★★★★★</div><div class="price">$42.00</div>
    <div class="btn">HOW TO VIDEO</div>
  </div>
  <div class="product" style="left:778px">
    <div class="product-img" role="img" aria-label="Product photo: concealer click pen"></div>
    <div class="product-name">CONCEALER</div><div class="stars">★★★★★</div><div class="price">$42.00</div>
    <div class="btn">HOW TO VIDEO</div>
  </div>
  <div class="dots" style="left:511px;top:600px"><i class="on" style="border-color:var(--gold);background:var(--gold)"></i><i style="border-color:var(--gold)"></i></div>
</section>

<div class="skincare-frame"></div>
<div class="photo skincare-photo" role="img" aria-label="Man kneeling in splashing sea water"></div>
<div class="skincare-card">USING OUR BEST SKINCARE MEN'S PRODUCTS</div>
<ul class="checklist">
  <li><svg width="18" height="18" viewBox="0 0 18 18"><circle cx="9" cy="9" r="8" stroke="#b07c2c" stroke-width="1.5" fill="none"/><path d="M5 9l3 3 5-6" stroke="#b07c2c" stroke-width="1.8" fill="none"/></svg>Lorem Ipsum is simply dumm</li>
  <li><svg width="18" height="18" viewBox="0 0 18 18"><circle cx="9" cy="9" r="8" stroke="#b07c2c" stroke-width="1.5" fill="none"/><path d="M5 9l3 3 5-6" stroke="#b07c2c" stroke-width="1.8" fill="none"/></svg>Lorem Ipsum is simply</li>
  <li><svg width="18" height="18" viewBox="0 0 18 18"><circle cx="9" cy="9" r="8" stroke="#b07c2c" stroke-width="1.5" fill="none"/><path d="M5 9l3 3 5-6" stroke="#b07c2c" stroke-width="1.8" fill="none"/></svg>Lorem Ipsum is simply text</li>
  <li><svg width="18" height="18" viewBox="0 0 18 18"><circle cx="9" cy="9" r="8" stroke="#b07c2c" stroke-width="1.5" fill="none"/><path d="M5 9l3 3 5-6" stroke="#b07c2c" stroke-width="1.8" fill="none"/></svg>Lorem Ipsum is simply dumm</li>
  <li><svg width="18" height="18" viewBox="0 0 18 18"><circle cx="9" cy="9" r="8" stroke="#b07c2c" stroke-width="1.5" fill="none"/><path d="M5 9l3 3 5-6" stroke="#b07c2c" stroke-width="1.8" fill="none"/></svg>Lorem Ipsum is simply</li>
  <li><svg width="18" height="18" viewBox="0 0 18 18"><circle cx="9" cy="9" r="8" stroke="#b07c2c" stroke-width="1.5" fill="none"/><path d="M5 9l3 3 5-6" stroke="#b07c2c" stroke-width="1.8" fill="none"/></svg>Lorem Ipsum is simply text</li>
  <li><svg width="18" height="18" viewBox="0 0 18 18"><circle cx="9" cy="9" r="8" stroke="#b07c2c" stroke-width="1.5" fill="none"/><path d="M5 9l3 3 5-6" stroke="#b07c2c" stroke-width="1.8" fill="none"/></svg>Lorem Ipsum is simply</li>
  <li><svg width="18" height="18" viewBox="0 0 18 18"><circle cx="9" cy="9" r="8" stroke="#b07c2c" stroke-width="1.5" fill="none"/><path d="M5 9l3 3 5-6" stroke="#b07c2c" stroke-width="1.8" fill="none"/></svg>Lorem Ipsum is simply text</li>
</ul>

<h2 class="section-title" style="top:2618px">#PICTURLOOP HITS</h2>
<div class="insta" style="left:78px;background:linear-gradient(150deg,#e8e4df 0%,#b58c6e 50%,#4a3a30 100%)" role="img" aria-label="Tattooed shirtless man posing"><span class="tag">#Corvane Sable</span></div>
<div class="insta" style="left:440px;background:linear-gradient(150deg,#f1f1f1 0%,#8d7a6c 50%,#2e2620 100%)" role="img" aria-label="Man with long dark hair and beard"><span class="tag">#Corvane Sable</span></div>
<div class="insta" style="left:798px;background:linear-gradient(150deg,#dcd6cf 0%,#a98670 50%,#3b2f27 100%)" role="img" aria-label="Man in a white shirt holding a cigar"><span class="tag">#Corvane Sable</span></div>
<div class="btn follow-btn"><svg width="16" height="16" viewBox="0 0 16 16"><rect x="1" y="1" width="14" height="14" rx="2" fill="#fff"/></svg>FOLLOW US</div>

<section class="testimonial" role="img" aria-label="Dark close-up of a man's eyes behind the testimonial">
  <h2 class="section-title">OVER 250,000+ HAPPY CUSTOMERS</h2>
  <div class="avatar" role="img" aria-label="Smiling customer portrait"></div>
  <p class="quote">" Lorem Ipsum is simply dummy text of the printing and typesetting industry. Lorem Ipsum has been the industry's standard ever since the "Lorem Ipsum is simply dummy text of the printing "</p>
  <div class="client">— &nbsp;CLIENT NAME</div>
  <div class="dots" style="left:565px;top:318px"><i class="on" style="border-color:var(--gold);background:var(--gold)"></i><i></i><i></i><i></i></div>
</section>

<h2 class="section-title" style="top:3532px">LATEST BLOG</h2>
<article class="blog-card" style="left:84px;width:337px">
  <div class="blog-date"><svg width="16" height="16" viewBox="0 0 16 16"><rect x="1" y="3" width="14" height="12" rx="1" fill="#b07c2c"/><rect x="3" y="7" width="10" height="6" fill="#fff"/></svg>06 August 2018</div>
  <div class="blog-rule"></div>
  <h3 class="blog-title">Lorem Ipsum is simply dummy text of the printing &amp; type</h3>
  <p class="blog-excerpt">Lorem Ipsum is simply dummy text of the printing and typesetting industry.</p>
  <div class="blog-img" style="background:linear-gradient(120deg,#2a2a2a,#8a8a8a 50%,#d0d0d0)" role="img" aria-label="Black and white portrait of a man"></div>
</article>
<article class="blog-card" style="left:440px;width:324px">
  <div class="blog-date"><svg width="16" height="16" viewBox="0 0 16 16"><rect x="1" y="3" width="14" height="12" rx="1" fill="#b07c2c"/><rect x="3" y="7" width="10" height="6" fill="#fff"/></svg>06 August 2018</div>
  <div class="blog-rule"></div>
  <h3 class="blog-title">Lorem Ipsum is simply dummy text of the printing &amp; type</h3>
  <p class="blog-excerpt">Lorem Ipsum is simply dummy text of the printing and typesetting industry.</p>
  <div class="blog-img" style="background:linear-gradient(120deg,#5d8297,#b9cdd8 50%,#3e5a6a)" role="img" aria-label="Man relaxing with a face mask"></div>
</article>
<article class="blog-card" style="left:785px;width:328px">
  <div class="blog-date"><svg width="16" height="16" viewBox="0 0 16 16"><rect x="1" y="3" width="14" height="12" rx="1" fill="#b07c2c"/><rect x="3" y="7" width="10" height="6" fill="#fff"/></svg>06 August 2018</div>
  <div class="blog-rule"></div>
  <h3 class="blog-title">Lorem Ipsum is simply dummy text of the printing &amp; type</h3>
  <p class="blog-excerpt">Lorem Ipsum is simply dummy text of the printing and typesetting industry.</p>
  <div class="blog-img" style="background:linear-gradient(120deg,#2b3440,#7b6c62 50%,#c9c4be)" role="img" aria-label="Bearded man in winter snow"></div>
</article>

<section class="rewards">
  <h2>REWARDS SIGN UP</h2>
  <p>Signup to receive rewards, new product arrivals, special deals, and exclusive offers.</p>
  <div class="email-field">Enter Email*</div>
  <div class="subscribe">SUBSCRIBE</div>
</section>

<footer class="site-footer">
  <div class="foot-col" style="left:78px"><h4>SITEMAP</h4><ul><li>Home</li><li>Our Store</li><li>Products</li><li>Blog</li><li>About Us</li><li>Contact Us</li></ul></div>
  <div class="foot-col" style="left:234px"><h4>CUSTOMER SERVICES</h4><ul><li>Contact Us</li><li>Delivery Information</li><li>Refunds and returns</li><li>Voucher Codes</li></ul></div>
  <div class="foot-col" style="left:489px"><h4>PRODUCTS</h4><ul><li>Face Cleanser</li><li>Mask</li><li>Moisturizer</li><li>Concealer</li><li>Liquid Liner</li><li>Setting Spray</li></ul></div>
  <div class="foot-col social" style="left:711px"><h4>FOLLOW US</h4><ul><li><span class="social-dot"></span>Friendwall</li><li><span class="social-dot"></span>Vidstream</li><li><span class="social-dot"></span>Vidstream</li><li><span class="social-dot"></span>Chirpline</li></ul></div>
  <div class="foot-col" style="left:926px"><h4>TERMS &amp; CONDITION</h4><ul><li>Privacy policy</li><li>Terms &amp; conditions</li><li>Cookie information</li></ul></div>
  <div class="foot-brand"><span class="brand-square"></span>CORVANE SABLE</div>
  <div class="copyright">© CORVANE SABLE - 2018 All RightReserved.</div>
</footer>

</body>
</html>
```